Esthetically Pleasing Core Values and Brand Promise for Accounting Firm

I would like a cohesive design that ties together my core values and brand promise. My firm, Maple Finch Advisory, provides accounting work to small businesses. I prefer modern and clean designs. I want my Core Values and Brand Promise to represent me - sole entrepreneur, married, mother of two kids, modern esthetics, clean lines, organized, colorful (teals, greys, white, yellows)

Industry/Entity Type

Public Accounting

Colors
33b8a4

```html
<!DOCTYPE html>
<html lang="en">
<head>
<meta charset="utf-8">
<title>Maple Finch Advisory – Core Values</title>
<link href="https://fonts.googleapis.com/css2?family=Alegreya+Sans:wght@400;500&family=Josefin+Sans:wght@300&family=Montserrat:wght@500;600&family=Orbitron:wght@800&family=Signika:wght@600;700&display=swap" rel="stylesheet">
<style>
  :root{
    --teal:#00999a;
    --teal-deep:#007f80;
    --teal-bright:#2fd0bf;
    --charcoal:#3f403f;
    --header-grey:#efefef;
    --ink:#3a3a3a;
    --white:#ffffff;
    --line-grey:#c9c9c9;
  }
  *{box-sizing:border-box;margin:0;padding:0}
  html,body{width:970px;height:1200px;overflow:hidden;background:var(--white)}
  .sheet{position:relative;width:970px;height:1200px;background:var(--white);overflow:hidden;font-family:"Alegreya Sans",sans-serif;color:var(--ink)}

  /* header */
  .masthead{position:absolute;left:12px;top:10px;width:946px;height:252px;background:var(--header-grey)}
  .brand-name{position:absolute;left:44px;top:48px;font-family:"Josefin Sans",sans-serif;font-weight:300;color:var(--teal);line-height:1}
  .brand-name span{display:block}
  .brand-name .line-1{font-size:64px;letter-spacing:2px}
  .brand-name .line-2{font-size:64px;letter-spacing:2px;margin-top:8px}
  .brand-name .line-3{font-size:40px;letter-spacing:3px;margin-top:14px}
  .hero-visual{position:absolute;left:470px;top:0;width:480px;height:300px}

  /* values */
  .connectors{position:absolute;left:0;top:0;width:970px;height:1200px}
  .values-wheel{position:absolute;left:218px;top:321px;width:520px;height:520px}
  .wheel-title{font-family:"Signika",sans-serif;font-weight:700;fill:var(--teal);text-anchor:middle}
  .value{position:absolute;width:300px}
  .value h2{font-family:"Signika",sans-serif;font-weight:700;font-size:27px;color:var(--teal);line-height:1;margin-bottom:6px}
  .value p{font-size:19px;line-height:24px;color:var(--ink)}
  .value--left{left:48px;text-align:left}
  .value--right{right:43px;text-align:right}
  .value--top{top:300px}
  .value--bottom{top:766px}

  /* promise */
  .promise-banner{position:absolute;left:0;top:893px;width:970px;height:38px;background:var(--teal);color:var(--white);font-family:"Signika",sans-serif;font-weight:700;font-size:26px;text-align:center;line-height:40px}
  .services{position:absolute;left:0;top:931px;width:970px;height:162px;background:var(--charcoal)}
  .service{position:absolute;top:13px;width:436px;height:132px;border:1.5px solid var(--teal);border-radius:14px;overflow:hidden;display:flex}
  .service--tax{left:44px}
  .service--accounting{left:491px}
  .service-icon{width:73px;background:var(--teal);display:flex;align-items:center;justify-content:center;flex-shrink:0}
  .service-body{padding:14px 14px 0 16px;color:var(--white)}
  .service-body h3{font-family:"Signika",sans-serif;font-weight:700;font-size:19px;line-height:1;margin-bottom:4px}
  .service-body p{font-size:17px;line-height:20px}

  /* footer */
  .footer{position:absolute;left:0;top:1093px;width:970px;height:107px;background:var(--teal-deep)}
  .footer-phone-band{position:absolute;left:0;top:0;width:620px;height:66px;background:var(--teal);clip-path:polygon(0 0,100% 0,96% 100%,0 100%)}
  .phone{position:absolute;left:46px;top:12px;display:flex;align-items:center;gap:10px;color:var(--white);font-family:"Orbitron",sans-serif;font-weight:800;font-size:44px;letter-spacing:2px;line-height:1}
  .web{position:absolute;left:48px;top:76px;color:var(--white);font-family:"Montserrat",sans-serif;font-weight:500;font-size:14px;letter-spacing:8.6px}
  .address{position:absolute;left:660px;top:22px;color:var(--white);font-family:"Montserrat",sans-serif;font-weight:500;font-size:14.5px;line-height:20px}
  .address strong{font-weight:600;font-size:15.5px}
</style>
</head>
<body>
<main class="sheet">

  <header class="masthead">
    <div class="brand-name">
      <span class="line-1">MAPLE</span>
      <span class="line-2">FINCH</span>
      <span class="line-3">ADVISORY</span>
    </div>
  </header>

  <svg class="hero-visual" viewBox="0 0 480 300" role="img" aria-label="Teal financial charts and stock data screen inside a circular frame">
    <defs>
      <radialGradient id="heroFill" cx="45%" cy="40%" r="70%">
        <stop offset="0" stop-color="#3fd3c2"/>
        <stop offset="0.55" stop-color="#128f8c"/>
        <stop offset="1" stop-color="#0a4f55"/>
      </radialGradient>
    </defs>
    <circle cx="210" cy="115" r="185" fill="#ffffff"/>
    <circle cx="210" cy="115" r="166" fill="url(#heroFill)"/>
  </svg>

  <svg class="connectors" viewBox="0 0 970 1200" aria-hidden="true">
    <g fill="none" stroke-width="3">
      <polyline points="141,414 141,501 270,501" stroke="var(--teal)"/>
      <polyline points="828,414 828,501 690,501" stroke="var(--charcoal)"/>
      <polyline points="141,748 141,661 270,661" stroke="var(--charcoal)"/>
      <polyline points="828,748 828,661 690,661" stroke="var(--teal)"/>
    </g>
    <circle cx="141" cy="414" r="7" fill="var(--teal)"/>
    <circle cx="828" cy="414" r="7" fill="var(--charcoal)"/>
    <circle cx="141" cy="748" r="7" fill="var(--charcoal)"/>
    <circle cx="828" cy="748" r="7" fill="var(--teal)"/>
  </svg>

  <svg class="values-wheel" viewBox="0 0 520 520" aria-label="Core values wheel">
    <defs>
      <filter id="softShadow" x="-10%" y="-10%" width="120%" height="120%">
        <feDropShadow dx="0" dy="2" stdDeviation="6" flood-color="#000" flood-opacity="0.18"/>
      </filter>
      <radialGradient id="hubFill" cx="50%" cy="40%" r="60%">
        <stop offset="0" stop-color="#ffffff"/>
        <stop offset="1" stop-color="#e4e6ea"/>
      </radialGradient>
    </defs>
    <circle cx="260" cy="260" r="256" fill="#fff" filter="url(#softShadow)"/>
    <path d="M260 260 L20 260 A240 240 0 0 1 260 20 Z" fill="var(--teal)"/>
    <path d="M260 260 L260 20 A240 240 0 0 1 500 260 Z" fill="var(--charcoal)"/>
    <path d="M260 260 L20 260 A240 240 0 0 0 260 500 Z" fill="var(--charcoal)"/>
    <path d="M260 260 L500 260 A240 240 0 0 1 260 500 Z" fill="var(--teal)"/>

    <circle cx="260" cy="260" r="114" fill="#fff"/>
    <circle cx="260" cy="260" r="110" fill="none" stroke="var(--line-grey)" stroke-width="1.5"/>
    <circle cx="260" cy="260" r="98" fill="none" stroke="var(--teal-bright)" stroke-width="7"/>
    <circle cx="260" cy="260" r="92" fill="none" stroke="var(--teal)" stroke-width="3"/>
    <circle cx="260" cy="260" r="88" fill="url(#hubFill)"/>
    <text class="wheel-title" x="260" y="252" font-size="42">CORE</text>
    <text class="wheel-title" x="260" y="296" font-size="42">VALUES</text>

    <!-- empower: crosshair with raised hand -->
    <g transform="translate(130 151)" stroke="#fff" fill="none" stroke-width="3">
      <circle r="36"/>
      <line x1="0" y1="-46" x2="0" y2="-28"/><line x1="0" y1="28" x2="0" y2="46"/>
      <line x1="-46" y1="0" x2="-28" y2="0"/><line x1="28" y1="0" x2="46" y2="0"/>
      <rect x="-10" y="-10" width="20" height="16" rx="4"/>
      <line x1="-6" y1="6" x2="-6" y2="16"/><line x1="6" y1="6" x2="6" y2="16"/>
    </g>
    <!-- rectitude: scales -->
    <g transform="translate(384 152)" stroke="#fff" fill="none" stroke-width="3">
      <circle r="38"/>
      <line x1="0" y1="-20" x2="0" y2="22"/>
      <line x1="-22" y1="-10" x2="22" y2="-10"/>
      <path d="M-30 8 L-22 -10 L-14 8 Z"/><path d="M14 8 L22 -10 L30 8 Z"/>
      <line x1="-10" y1="22" x2="10" y2="22"/>
    </g>
    <!-- client focused: crosshair with dot -->
    <g transform="translate(142 371)" stroke="#fff" fill="none" stroke-width="3">
      <circle r="36"/>
      <line x1="0" y1="-46" x2="0" y2="-28"/><line x1="0" y1="28" x2="0" y2="46"/>
      <line x1="-46" y1="0" x2="-28" y2="0"/><line x1="28" y1="0" x2="46" y2="0"/>
      <circle r="8" fill="#fff"/>
    </g>
    <!-- relentless: lightning -->
    <g transform="translate(377 378)" stroke="#fff" stroke-width="3">
      <circle r="36" fill="none"/>
      <path d="M8 -26 L-14 4 L0 4 L-8 26 L16 -6 L2 -6 Z" fill="#fff" stroke-linejoin="round"/>
    </g>
  </svg>

  <section class="value value--left value--top">
    <h2>EMPOWER</h2>
    <p>We are dedicated, appreciative and respectful of people’s time and purpose.</p>
  </section>
  <section class="value value--right value--top">
    <h2>RECTITUDE</h2>
    <p>We know the difference between what we have the right to do and what the right thing to do is.</p>
  </section>
  <section class="value value--left value--bottom">
    <h2>CLIENT FOCUSED</h2>
    <p>We provide a personal service that goes above the standards of professional care.</p>
  </section>
  <section class="value value--right value--bottom">
    <h2>RELENTLESS</h2>
    <p>We believe that the longer we try to do our best, the better we become.</p>
  </section>

  <div class="promise-banner">TRUST, TRANSPARENCY AND DEPENDABILITY</div>

  <section class="services">
    <article class="service service--tax">
      <div class="service-icon">
        <svg width="50" height="42" viewBox="0 0 50 42" fill="none" stroke="#fff" stroke-width="2">
          <rect x="4" y="4" width="34" height="32" rx="4"/>
          <line x1="1" y1="8" x2="1" y2="32"/>
          <line x1="10" y1="13" x2="32" y2="13"/><line x1="10" y1="18" x2="32" y2="18"/><line x1="10" y1="23" x2="26" y2="23"/>
          <circle cx="40" cy="32" r="8" fill="var(--teal)"/>
          <text x="40" y="36.5" font-size="12" fill="#fff" stroke="none" text-anchor="middle" font-family="Montserrat, sans-serif">$</text>
        </svg>
      </div>
      <div class="service-body">
        <h3>TAX</h3>
        <p>Maple Finch provides all clients with a trusted tax advisor who provides accuracy in all filings and ensures your compliance with all government agencies.</p>
      </div>
    </article>
    <article class="service service--accounting">
      <div class="service-icon">
        <svg width="50" height="42" viewBox="0 0 50 42" fill="none" stroke="#fff" stroke-width="2">
          <rect x="4" y="4" width="34" height="32" rx="4"/>
          <line x1="1" y1="8" x2="1" y2="32"/>
          <line x1="10" y1="13" x2="28" y2="13"/><line x1="10" y1="18" x2="28" y2="18"/>
          <rect x="28" y="20" width="18" height="18" fill="var(--teal)"/>
          <line x1="34" y1="20" x2="34" y2="38"/><line x1="40" y1="20" x2="40" y2="38"/>
          <line x1="28" y1="26" x2="46" y2="26"/><line x1="28" y1="32" x2="46" y2="32"/>
        </svg>
      </div>
      <div class="service-body">
        <h3>ACCOUNTING</h3>
        <p>Maple Finch provides all business owners with the financial visibility needed to foster growth and facilitate goals.</p>
      </div>
    </article>
  </section>

  <footer class="footer">
    <div class="footer-phone-band"></div>
    <div class="phone">
      <svg width="26" height="26" viewBox="0 0 24 24" fill="#fff" aria-hidden="true">
        <path d="M6.6 10.8a15.1 15.1 0 0 0 6.6 6.6l2.2-2.2c.3-.3.7-.4 1-.2 1.1.4 2.3.6 3.6.6.6 0 1 .4 1 1V20c0 .6-.4 1-1 1A17 17 0 0 1 3 4c0-.6.4-1 1-1h3.5c.6 0 1 .4 1 1 0 1.3.2 2.5.6 3.6.1.3 0 .7-.2 1z"/>
      </svg>
      <span>555.204.7731</span>
    </div>
    <div class="web">www.maplefinchadvisory.com</div>
    <address class="address" style="font-style:normal">
      <strong>Maple Finch Advisory</strong><br>
      1180 W. Orchard Avenue, Suite<br>
      300 Linden Park, CA&nbsp; 90000
    </address>
  </footer>

</main>
</body>
</html>
```